Real Estate Investment Company needs postcard design

We need a postcard design for a Real Estate Investment company named 'Brightpath Homestead Partners, LLC'. We are a residential redevelopment company who specializes in buying distressed homes at a significant discount, and renovate and resell them to retail home buyers and landlords. Our service is to give home owners an option to contact us if they want to sell their home. We would like to see designs that use our logo with a modern and friendly feel. These post cards will be going out to clients who are in stressful situations (foreclosure, estate sales, etc.) and would like them to feel comfortable and safe when receiving this postcard. The final design should communicate stress free and fast solution for their situation.
Real Estate

```html
<!DOCTYPE html>
<html lang="en">
<head>
<meta charset="utf-8">
<title>Brightpath Homestead Partners – Postcard</title>
<link href="https://fonts.googleapis.com/css2?family=Roboto+Condensed:ital,wght@0,400;0,700;1,700&family=Open+Sans:wght@400;600&display=swap" rel="stylesheet">
<style>
  :root{
    --blue:#0c72bd;
    --gray:#6a6a6a;
    --white:#ffffff;
    --ink:#141414;
    --stage:#e4e4e2;
    --photo-warm:#d9a877;
    --photo-stone:#b6a58a;
  }
  *{box-sizing:border-box;margin:0;padding:0}
  html,body{width:1200px;height:960px;overflow:hidden;background:var(--stage)}
  .canvas{position:relative;width:1200px;height:960px}
  .card{position:absolute;width:600px;height:400px;background:var(--white);overflow:hidden;box-shadow:0 6px 18px rgba(0,0,0,.18)}
  .card-bg{position:absolute;inset:0}
  .front{left:40px;top:50px}
  .back{left:560px;top:500px}

  .headline{position:absolute;left:28px;top:62px;width:270px;color:var(--white);font:700 26px/1.12 "Roboto Condensed",sans-serif}
  .photo{position:absolute;border:4px solid #111}
  .photo-room{left:300px;top:118px;width:172px;height:112px;background:linear-gradient(135deg,#f1d2a8,var(--photo-warm) 60%,#a6532b)}
  .photo-fireplace{left:424px;top:18px;width:152px;height:164px;background:radial-gradient(circle at 50% 55%,#2b2b2b 0 28%,#c9c9c9 29% 38%,var(--photo-stone) 39%)}

  .col{position:absolute;color:var(--white);font-family:"Open Sans",sans-serif}
  .col-left{left:30px;top:200px;width:225px}
  .col-right{left:286px;top:244px;width:200px}
  .intro{font-size:12.5px;line-height:1.3;margin-bottom:4px}
  .col-title{font:italic 700 15px/1.25 "Roboto Condensed",sans-serif;margin-bottom:1px}
  .bullets{list-style:none;font-size:12px;line-height:1.3}
  .bullets li::before{content:"★";font-size:8px;margin-right:7px;vertical-align:2px}
  .divider{position:absolute;left:270px;top:200px;width:1px;height:122px;background:rgba(255,255,255,.6)}

  .brand{position:absolute;display:flex;align-items:center;gap:10px;color:var(--blue);font:700 24px/1.05 "Roboto Condensed",sans-serif}
  .brand-mark{width:14px;height:14px;background:var(--blue);flex:none}
  .front .brand{left:70px;top:362px;white-space:nowrap}
  .back .brand{left:30px;top:86px}

  .contact{position:absolute;left:32px;top:190px;font:400 17px/1.4 "Open Sans",sans-serif;color:var(--ink)}
  .stamp{position:absolute;left:482px;top:28px;width:82px;height:88px;border:2px solid #666}
  .address-line{position:absolute;left:370px;width:205px;height:2px;background:var(--ink)}
  .tagline{position:absolute;left:50px;top:360px;color:var(--white);font:400 19px/1 "Open Sans",sans-serif}
</style>
</head>
<body>
<div class="canvas">

  <section class="card front" aria-label="Postcard front">
    <svg class="card-bg" width="600" height="400" viewBox="0 0 600 400" aria-hidden="true">
      <rect width="600" height="400" fill="var(--blue)"/>
      <polygon points="0,0 600,0 600,130 300,130 300,190 0,190" fill="var(--gray)"/>
      <polygon points="490,400 490,300 600,300 600,400" fill="var(--white)"/>
      <polygon points="18,400 18,372 50,344 100,358 300,340 600,340 600,400" fill="var(--white)"/>
    </svg>
    <h1 class="headline">Lorem ipsum dolor sit amet<br>consectetuer adipis</h1>
    <div class="photo photo-room" role="img" aria-label="Photo of a bright renovated bedroom"></div>
    <div class="photo photo-fireplace" role="img" aria-label="Photo of a modern fireplace set in a stone wall"></div>

    <div class="col col-left">
      <p class="intro">Lorem ipsum dolor sit amet<br>consectetuer</p>
      <p class="col-title">Lorem ipsum dolor</p>
      <ul class="bullets"><li>Lorem ipsum dolor</li><li>Lorem ipsum dolor</li><li>Lorem ipsum dolor</li><li>Lorem ipsum dolor</li></ul>
    </div>
    <div class="divider"></div>
    <div class="col col-right">
      <p class="col-title">Lorem ipsum dolor</p>
      <ul class="bullets"><li>Lorem ipsum dolor</li><li>Lorem ipsum dolor</li><li>Lorem ipsum dolor</li><li>Lorem ipsum dolor</li></ul>
    </div>

    <div class="brand"><span class="brand-mark"></span><span>Brightpath Homestead Partners</span></div>
  </section>

  <section class="card back" aria-label="Postcard back">
    <svg class="card-bg" width="600" height="400" viewBox="0 0 600 400" aria-hidden="true">
      <rect width="600" height="400" fill="var(--white)"/>
      <rect x="0" y="0" width="325" height="50" fill="var(--gray)"/>
      <polygon points="0,400 0,362 42,322 98,336 318,300 345,400" fill="var(--blue)"/>
    </svg>
    <div class="brand"><span class="brand-mark"></span><span>Brightpath Homestead<br>Partners</span></div>
    <p class="contact">P: 555-010-0199<br>E: hello@brightpathhomestead.com<br>W: www.brightpathhomestead.com</p>
    <div class="stamp" aria-label="Stamp area"></div>
    <div class="address-line" style="top:222px"></div>
    <div class="address-line" style="top:252px"></div>
    <div class="address-line" style="top:282px"></div>
    <p class="tagline">Lorem ipsum dolor</p>
  </section>

</div>
</body>
</html>
```